Custom Framing Shop Stonebrook Framing Studio

I want an eye catching graphic that will be used a s business sign on a busy road. The sign MUST communicate the type of business it is clearly to vehicles traveling at 40 mph. This is a custom picture framing business and the sign will be hanging and be approximately 32" X 48". The business name is Stonebrook Framing Studio; Custom framing: by appointment and should include a whole or partial image of a picture frame as a visual que. I've included inspiration idea's, color pallets and styles that I like and a current business card for inspiration. I like the crimson font style shadowing and background colors of the attached Pello's pizzeria sign. I'd prefer crimson letters. Custom Framing is the message to communicate, followed by phone number and business name. I like the idea of a shield shape with a banner since it would more eye catching, Once again the Stonebrook image and name is less important than communicating what the business does. I like Crimson, grey, gold, black but am open to new ideas . I like the idea of a shield with a banner more than a rectangle, but am open to idea's

Target Market(s)

My target market is local homeowners ($700k+) who want a relationship with their framer and are willing to pay for a customized experience compared to a craft store experience. I have more female clients then men.

Industry/Entity Type

Picture Framing Art

Other font styles liked:
• Look at the attached image of a custom pizzeria sign, its kid of a custom car pinstripe font style. Script and decorative may be difficult to read while driving by but add to the elegance.

Colors

Designer to choose colors to be used in the design.

Requirements
Must have
• Clearly communicate what the business does "Custom framing" preferably with a picture frame and words
Nice to have
• incorporate a Stonebrook into the graphic
Should not have
• A Stonebrook image doesn't communicate what the business does to a vehicle traveling at 40 mph by the sign

```html
<!DOCTYPE html>
<html lang="en">
<head>
<meta charset="utf-8">
<title>Stonebrook Framing Studio – Custom Framing Sign</title>
<link rel="stylesheet" href="https://fonts.googleapis.com/css2?family=Rye&family=Cinzel:wght@400;700&family=Oswald:wght@500&display=swap">
<style>
  :root {
    --crimson: #8a1f22;
    --crimson-shadow: #2a2a2a;
    --black: #171716;
    --gold: #d1b05a;
    --gold-light: #ecd982;
    --gold-deep: #b8902e;
    --amber: #d68a2a;
    --cream: #fde8de;
    --white: #ffffff;
    --bg: #ffffff;
  }
  html, body {
    margin: 0;
    padding: 0;
    width: 800px;
    height: 1200px;
    overflow: hidden;
    background: var(--bg);
  }
  .sign {
    display: block;
    width: 800px;
    height: 1200px;
  }
  .shield-body { fill: var(--black); }
  .shield-trim { fill: none; stroke: var(--gold); stroke-width: 16; }
  .crest-disc { fill: var(--gold); }
  .crest-disc-inner { fill: var(--gold-light); }
  .crest-name {
    font-family: "Rye", serif;
    font-size: 64px;
    fill: var(--crimson);
  }
  .title-band { fill: var(--gold); }
  .title-name {
    font-family: "Rye", serif;
    font-size: 190px;
    fill: var(--crimson);
    stroke: var(--gold-light);
    stroke-width: 2;
    paint-order: stroke;
  }
  .title-name-shadow {
    font-family: "Rye", serif;
    font-size: 190px;
    fill: var(--crimson-shadow);
  }
  .rule { fill: none; stroke: var(--gold-deep); stroke-width: 4; }
  .rule-dot { fill: var(--gold-deep); }
  .studio-line {
    font-family: "Cinzel", serif;
    font-weight: 400;
    font-size: 76px;
    fill: var(--white);
  }
  .frame-moulding { fill: url(#mouldingGrad); }
  .frame-bevel { fill: none; stroke: var(--gold-deep); stroke-width: 6; }
  .frame-bead { fill: none; stroke: #a88530; stroke-width: 3; stroke-dasharray: 3 5; }
  .frame-panel { fill: url(#panelGrad); }
  .headline {
    font-family: "Rye", serif;
    font-size: 208px;
    fill: var(--crimson);
    stroke: #1a0d0d;
    stroke-width: 5;
    paint-order: stroke;
  }
  .ribbon-face { fill: url(#ribbonGrad); }
  .ribbon-tail { fill: url(#tailGrad); }
  .ribbon-fold { fill: #5a3418; }
  .ribbon-text {
    font-family: "Cinzel", serif;
    font-weight: 700;
    font-size: 66px;
    fill: #111111;
  }
  .phone {
    font-family: "Oswald", sans-serif;
    font-weight: 500;
    font-size: 158px;
    fill: var(--cream);
    stroke: #3a2a22;
    stroke-width: 4;
    paint-order: stroke;
  }
  .ornament { fill: var(--gold-deep); opacity: 0.55; }
</style>
</head>
<body>
<svg class="sign" viewBox="0 0 1568 2352" xmlns="http://www.w3.org/2000/svg" role="img" aria-label="Stonebrook Framing Studio sign: Custom Framing by appointment">
  <defs>
    <linearGradient id="mouldingGrad" x1="0" y1="0" x2="1" y2="0">
      <stop offset="0" stop-color="#f2df93"/>
      <stop offset="0.08" stop-color="#a87a22"/>
      <stop offset="0.18" stop-color="#e8cf7c"/>
      <stop offset="0.5" stop-color="#f0dc8c"/>
      <stop offset="0.82" stop-color="#e8cf7c"/>
      <stop offset="0.92" stop-color="#a87a22"/>
      <stop offset="1" stop-color="#f2df93"/>
    </linearGradient>
    <radialGradient id="panelGrad" cx="0.45" cy="0.45" r="0.7">
      <stop offset="0" stop-color="#efdd8a"/>
      <stop offset="0.6" stop-color="#ecd982"/>
      <stop offset="1" stop-color="#cfae58"/>
    </radialGradient>
    <linearGradient id="ribbonGrad" x1="0" y1="0" x2="1" y2="0">
      <stop offset="0" stop-color="#f8e07a"/>
      <stop offset="0.3" stop-color="#d99a38"/>
      <stop offset="0.55" stop-color="#cf8426"/>
      <stop offset="0.85" stop-color="#f9bd4e"/>
      <stop offset="1" stop-color="#c88a2c"/>
    </linearGradient>
    <linearGradient id="tailGrad" x1="0" y1="0" x2="1" y2="0">
      <stop offset="0" stop-color="#eea52e"/>
      <stop offset="1" stop-color="#4a2a12"/>
    </linearGradient>
    <radialGradient id="discGrad" cx="0.5" cy="0.45" r="0.55">
      <stop offset="0" stop-color="#c9a54a"/>
      <stop offset="0.6" stop-color="#e2c874"/>
      <stop offset="1" stop-color="#ecd982"/>
    </radialGradient>
    <path id="titleArc" d="M 110 880 Q 787 450 1470 880"/>
  </defs>

  <!-- Shield -->
  <path class="shield-body" d="M 35 415 Q 190 430 270 293 L 465 243 A 346 346 0 0 1 1108 243 L 1305 293 Q 1385 430 1540 415 L 1540 1805 Q 1420 1870 1420 2022 L 787 2338 L 155 2022 Q 155 1870 35 1805 Z"/>
  <path class="shield-trim" d="M 74 455 Q 240 470 295 332 L 480 288 L 1090 288 L 1280 332 Q 1340 470 1500 455 L 1500 1780 Q 1395 1845 1392 1998 L 787 2300 L 182 1998 Q 180 1845 74 1780 Z"/>

  <!-- Crest disc with name -->
  <g class="crest">
    <circle class="crest-disc" cx="787" cy="370" r="318"/>
    <circle cx="787" cy="370" r="290" fill="url(#discGrad)"/>
    <text class="crest-name" x="787" y="392" text-anchor="middle">Stonebrook</text>
  </g>

  <!-- Side ornaments -->
  <rect class="ornament" x="335" y="378" width="120" height="160" rx="40" role="img" aria-label="Gold filigree flourish"/>
  <rect class="ornament" x="1112" y="378" width="120" height="160" rx="40" role="img" aria-label="Gold filigree flourish"/>

  <!-- Title band -->
  <path class="title-band" d="M 82 640 Q 787 400 1490 640 L 1490 668 Q 787 440 82 668 Z"/>

  <!-- Business name -->
  <text class="title-name-shadow" text-anchor="middle" transform="translate(8 10)"><textPath href="#titleArc" startOffset="50%" textLength="1320" lengthAdjust="spacingAndGlyphs">STONEBROOK</textPath></text>
  <text class="title-name" text-anchor="middle"><textPath href="#titleArc" startOffset="50%" textLength="1320" lengthAdjust="spacingAndGlyphs">STONEBROOK</textPath></text>

  <!-- Divider under name -->
  <path class="rule" d="M 265 1005 Q 520 890 750 892"/>
  <path class="rule" d="M 1310 1005 Q 1055 890 825 892"/>
  <circle class="rule-dot" cx="752" cy="892" r="9"/>
  <circle class="rule-dot" cx="820" cy="892" r="9"/>
  <path class="rule-dot" d="M 787 868 L 811 892 L 787 916 L 763 892 Z"/>

  <!-- Framing Studio line -->
  <line class="rule" x1="265" y1="1040" x2="395" y2="1040"/>
  <path class="rule-dot" d="M 379 1030 L 389 1040 L 379 1050 L 369 1040 Z"/>
  <text class="studio-line" x="783" y="1066" text-anchor="middle" textLength="735" lengthAdjust="spacingAndGlyphs">FRAMING STUDIO</text>
  <line class="rule" x1="1172" y1="1040" x2="1308" y2="1040"/>
  <path class="rule-dot" d="M 1194 1030 L 1204 1040 L 1194 1050 L 1184 1040 Z"/>

  <!-- Picture frame -->
  <g class="picture-frame">
    <rect class="frame-moulding" x="158" y="1108" width="1237" height="657" role="img" aria-label="Ornate carved gold picture frame moulding"/>
    <rect class="frame-bevel" x="268" y="1180" width="1017" height="505"/>
    <rect class="frame-bead" x="288" y="1192" width="977" height="481"/>
    <rect class="frame-panel" x="302" y="1204" width="948" height="462"/>
  </g>

  <!-- Headline -->
  <text class="headline" x="772" y="1415" text-anchor="middle" textLength="640" lengthAdjust="spacingAndGlyphs">CUSTOM</text>
  <text class="headline" x="770" y="1618" text-anchor="middle" textLength="740" lengthAdjust="spacingAndGlyphs">FRAMING</text>

  <!-- Ribbon -->
  <g class="ribbon">
    <path class="ribbon-tail" d="M 205 1895 L 310 1822 L 235 1760 L 500 1760 L 500 1895 Z"/>
    <path class="ribbon-tail" d="M 1362 1895 L 1258 1822 L 1330 1760 L 1067 1760 L 1067 1895 Z" transform="scale(-1 1) translate(-2567 0)"/>
    <path class="ribbon-fold" d="M 356 1830 L 500 1895 L 500 1810 Z"/>
    <path class="ribbon-fold" d="M 1210 1830 L 1067 1895 L 1067 1810 Z"/>
    <path class="ribbon-face" d="M 356 1680 Q 783 1610 1210 1680 L 1210 1830 Q 783 1775 356 1833 Z"/>
    <text class="ribbon-text" x="780" y="1787" text-anchor="middle" textLength="745" lengthAdjust="spacingAndGlyphs">BY APPOINTMENT</text>
  </g>

  <!-- Small rule -->
  <line class="rule" x1="555" y1="1848" x2="1015" y2="1848" style="stroke-width:2"/>
  <path class="rule-dot" d="M 785 1840 L 795 1848 L 785 1856 L 775 1848 Z"/>

  <!-- Phone -->
  <text class="phone" x="792" y="2045" text-anchor="middle" textLength="805" lengthAdjust="spacingAndGlyphs">(360) 555-0148</text>

  <!-- Bottom ornament -->
  <ellipse class="ornament" cx="787" cy="2160" rx="90" ry="62" role="img" aria-label="Gold filigree flourish"/>
</svg>
</body>
</html>
```